Stationary set for consulting company
Tarvo Bridge
Creative Brief
Modern
Karim Yusuf Al Banna
Co-Founder
Reef Spire, Abu Dhabi United Arab Emirates
karim@tarvobridge.ae
www.tarvobridge.com
I need a full stationary set for the company logo I will be attaching. (PPTs, business cards, envelope, letterhead, etc)

```html
<!DOCTYPE html>
<html lang="en">
<head>
<meta charset="utf-8">
<title>Tarvo Bridge – Business Card</title>
<link href="https://fonts.googleapis.com/css2?family=Roboto:wght@400;500;700&display=swap" rel="stylesheet">
<style>
  :root {
    --page-bg: #e9e9ea;
    --brand-navy: #1f3d7e;
    --brand-navy-light: #2c4c92;
    --brand-sky: #7fb0de;
    --card-white: #ffffff;
    --text-grey: #7a7f88;
    --rule-grey: #c9ccd2;
  }
  * { margin: 0; padding: 0; box-sizing: border-box; }
  html, body { width: 1200px; height: 901px; overflow: hidden; }
  body {
    background: var(--page-bg);
    font-family: "Roboto", Arial, sans-serif;
    position: relative;
  }
  .card {
    position: absolute;
    left: 300px;
    width: 600px;
    height: 341px;
    border-radius: 14px;
  }
  .card-front {
    top: 68px;
    background: var(--brand-navy);
    display: flex;
    align-items: center;
    justify-content: center;
  }
  .front-wordmark {
    font-size: 40px;
    font-weight: 500;
    color: var(--brand-navy-light);
    letter-spacing: 1px;
  }
  .card-back {
    top: 487px;
    background: var(--card-white);
  }
  .back-brand {
    position: absolute;
    left: 22px;
    top: 136px;
    display: flex;
    align-items: center;
    gap: 12px;
  }
  .brand-dot {
    width: 26px; height: 26px;
    border-radius: 50%;
    background: var(--brand-sky);
  }
  .brand-name {
    font-size: 34px;
    font-weight: 700;
    color: var(--brand-navy);
    letter-spacing: 0.5px;
  }
  .divider {
    position: absolute;
    left: 299px;
    top: 80px;
    width: 1px;
    height: 175px;
    background: var(--rule-grey);
  }
  .contact-block {
    position: absolute;
    left: 316px;
    top: 86px;
  }
  .person-name {
    font-size: 21px;
    font-weight: 700;
    color: var(--brand-navy);
  }
  .person-role {
    font-size: 13px;
    color: var(--text-grey);
    margin-top: 4px;
  }
  .address {
    font-size: 13px;
    line-height: 18px;
    color: var(--text-grey);
    margin-top: 16px;
  }
  .contact-list {
    list-style: none;
    margin-top: 22px;
  }
  .contact-list li {
    display: flex;
    align-items: center;
    gap: 9px;
    font-size: 13px;
    line-height: 19px;
    color: var(--text-grey);
  }
  .contact-list svg { width: 11px; height: 11px; flex: none; }
</style>
</head>
<body>
  <section class="card card-front">
    <span class="front-wordmark">Tarvo Bridge</span>
  </section>

  <section class="card card-back">
    <div class="back-brand">
      <span class="brand-dot"></span>
      <span class="brand-name">Tarvo Bridge</span>
    </div>
    <div class="divider"></div>
    <div class="contact-block">
      <p class="person-name">Karim Yusuf Al Banna</p>
      <p class="person-role">Co-Founder</p>
      <p class="address">Reef Spire, Abu Dhabi<br>United Arab Emirates</p>
      <ul class="contact-list">
        <li>
          <svg viewBox="0 0 12 12" aria-hidden="true"><path d="M3 1 L5 3.5 L4 5 Q5.5 7.5 7 8 L8.5 7 L11 9 L9.5 11 Q4 10.5 1 3 Z" fill="#7a7f88"/></svg>
          +971-50-4417308
        </li>
        <li>
          <svg viewBox="0 0 12 12" aria-hidden="true"><rect x="1" y="2.5" width="10" height="7" rx="1" fill="#7a7f88"/><path d="M1.5 3 L6 6.5 L10.5 3" stroke="#fff" stroke-width="1" fill="none"/></svg>
          karim@tarvobridge.ae
        </li>
        <li>
          <svg viewBox="0 0 12 12" aria-hidden="true"><circle cx="6" cy="6" r="4.5" stroke="#7a7f88" stroke-width="1.2" fill="none"/><path d="M1.5 6 H10.5 M6 1.5 Q3.5 6 6 10.5 M6 1.5 Q8.5 6 6 10.5" stroke="#7a7f88" stroke-width="0.9" fill="none"/></svg>
          www.tarvobridge.com
        </li>
      </ul>
    </div>
  </section>
</body>
</html>
```